We are a team of QNV cloud specialists who obsessively empower customer organisations to feel confident in managing their growing QNV use, whatever their business needs are. As leading edge cloud artisans we do this by using our passion for simplification, reuse, automation, innovation and quality. We always put the 'customer journey' at the center of our many obsessions.

Target Market(s)

It's mainly a corporate market and we are targeting medium-sized businesses.

Industry/Entity Type

It Company

Contact Information for Business Card

Company name: Corvexo
Name
position
Phone
Web
Email

Font styles to use
Serif
Decorative

Colors

Designer to choose colors to be used in the design.

Requirements
Must have
• Must be funky and modern.
Nice to have
• Preferably embossed.

```html
<!DOCTYPE html>
<html lang="en">
<head>
<meta charset="utf-8">
<title>Corvexo Business Card</title>
<link href="https://fonts.googleapis.com/css2?family=Arvo:wght@400;700&display=swap" rel="stylesheet">
<style>
  :root {
    --stage: #0c1e2b;
    --card-light: #ffffff;
    --card-dark: #000000;
    --ink: #111111;
    --brand-orange: #f7931e;
    --brand-blue: #35b6f4;
  }
  * { margin: 0; padding: 0; box-sizing: border-box; }
  html, body {
    width: 1200px; height: 1200px; overflow: hidden;
    background: var(--stage);
    font-family: "Arvo", serif;
  }
  .canvas { position: relative; width: 1200px; height: 1200px; }
  .card {
    position: absolute; width: 646px; height: 356px; border-radius: 19px;
  }
  .card--front { left: 310px; top: 214px; background: var(--card-light); }
  .card--back { left: 307px; top: 611px; background: var(--card-dark); }

  .brand {
    position: absolute; display: flex; align-items: center; gap: 12px;
    color: var(--brand-orange); font-size: 36px; font-weight: 400;
    letter-spacing: 3px;
  }
  .brand__dot {
    width: 22px; height: 22px; border-radius: 50%; background: var(--brand-blue);
  }
  .card--front .brand { left: 72px; top: 150px; }
  .card--back .brand { left: 50%; top: 150px; transform: translateX(-50%); }

  .holder { position: absolute; left: 402px; top: 58px; color: var(--ink); }
  .holder__name { font-size: 21px; font-weight: 700; }
  .holder__role { font-size: 13px; margin-top: 4px; }

  .contacts { position: absolute; left: 402px; top: 160px; list-style: none; color: var(--ink); font-size: 12.5px; }
  .contacts li { display: flex; align-items: flex-start; gap: 10px; line-height: 21px; }
  .contacts li + li { margin-top: 4px; }
  .contacts li.address { margin-bottom: 6px; }
  .contacts svg { width: 14px; height: 14px; flex: none; margin-top: 4px; fill: var(--brand-orange); }

  .back-web {
    position: absolute; left: 0; right: 0; top: 268px; text-align: center;
    color: var(--brand-blue); font-size: 17px;
  }
</style>
</head>
<body>
<main class="canvas">
  <section class="card card--front">
    <div class="brand"><span class="brand__dot"></span><span>CORVEXO</span></div>
    <div class="holder">
      <p class="holder__name">Your name</p>
      <p class="holder__role">Founder &amp; Director</p>
    </div>
    <ul class="contacts">
      <li class="address">
        <svg viewBox="0 0 14 14"><path d="M7 0a5 5 0 0 0-5 5c0 4 5 9 5 9s5-5 5-9a5 5 0 0 0-5-5zm0 7a2 2 0 1 1 0-4 2 2 0 0 1 0 4z"/></svg>
        <span>2240 Alder Row<br>Chicago, IL 60612</span>
      </li>
      <li>
        <svg viewBox="0 0 14 14"><path d="M3 0l2.5 3-1.5 2c1 2 2.5 3.5 4.5 4.5l2-1.5 3 2.5-1.5 3C6 13 1 8 0 1.5z"/></svg>
        <span>(555) 010 - 0000</span>
      </li>
      <li>
        <svg viewBox="0 0 14 14"><path d="M3 0h8v4H3zM1 5h12v6h-2V9H3v2H1zM4 10h6v4H4z"/></svg>
        <span>(555) 010 - 0000</span>
      </li>
      <li>
        <svg viewBox="0 0 14 14"><path d="M0 2h14v10H0zm1.5 1.5L7 8l5.5-4.5v-.2h-11z"/></svg>
        <span>info@corvexo.com</span>
      </li>
      <li>
        <svg viewBox="0 0 14 14"><path d="M7 0a7 7 0 1 0 0 14A7 7 0 0 0 7 0zm0 2a5 5 0 0 1 5 5H7z"/></svg>
        <span>www.corvexo.com</span>
      </li>
    </ul>
  </section>

  <section class="card card--back">
    <div class="brand"><span class="brand__dot"></span><span>CORVEXO</span></div>
    <p class="back-web">www.corvexo.com</p>
  </section>
</main>
</body>
</html>
```